COPPER MIST- New packaging design

Create new packaging design for Copper Mist.
We are looking to update our packaging design onto our new box.
Designer must be creative and produce all the required elements as needed.
Designer will create new packaging layout, change color scheme of logo as needed, create new background design, etc.
Please use Example designs as reference. These are the companies/ designs we want to resemble.
Design die-line and guideline files are attached.
FRONT DESIGN OF BOX:
Attached to the files is our OLD PACKAGING file that we currently use. Most of the design will be transferred over with the addition of the CA Instituted THC label (file attached)
-Copper Mist logo
-THC label
-"500mg"
-"Net WT .5g"
BACK DESIGN OF BOX:
Attached to the files is BACK EXAMPLE file. We need most of the info in the back transferred over to the new box dieline.
-Directions:
1. Remove vaporizer cartridge from package and remove rubber stoppers.
2. Screw Cartridge clockwise onto any 510 threaded battery of your choice.
-Store at room temperature.
Direct sunlight and excessive heat may cause the cartridge to leak.
-"GOVERNMENT WARNING: THIS PRODUCT CONTAINS CANNABIS, A SCHEDULE I CONTROLLED SUBSTANCE. KEEP OUT OF REACH OF CHILDREN AND ANIMALS. CANNABIS PRODUCTS MAY ONLY BE POSSESSED OR CONSUMED BY PERSONS 21 YEARS OF AGE OR OLDER UNLESS THE PERSON IS A QUALIFIED PATIENT. THE INTOXICATING EFFECTS OF CANNABIS PRODUCTS MAY BE DELAYED UP TO TWO HOURS. CANNABIS USE WHILE PREGNANT OR BREASTFEEDING MAY BE HARMFUL. CONSUMPTION OF CANNABIS PRODUCTS IMPAIRS YOUR ABILITY TO DRIVE AND OPERATE MACHINERY. PLEASE USE EXTREME CAUTION."
INNER TRAY OF BOX:
(will be designed after outer carton of box is finished)

```html
<!DOCTYPE html>
<html lang="en">
<head>
<meta charset="utf-8">
<title>Copper Mist – Packaging Options</title>
<link href="https://fonts.googleapis.com/css2?family=Open+Sans:wght@400;700&family=Rye&display=swap" rel="stylesheet">
<style>
  :root {
    --stage: #e8e8e8;
    --box-dark: #151515;
    --box-light: #f5f5f5;
    --gold: #c9a33c;
    --leaf-green: #4c9b30;
    --lime: #8cc63f;
    --band-dark: #1b1b1b;
    --oil: #f2b51c;
    --mark-grey: #7a7a7a;
    --label-grey: #8a8a8a;
    --cream: #f3ecd2;
    --dose-dark: #1c3d12;
  }
  html, body {
    margin: 0;
    padding: 0;
    width: 1200px;
    height: 884px;
    overflow: hidden;
    background: var(--stage);
  }
  .canvas {
    position: relative;
    width: 1200px;
    height: 884px;
  }
  .carton {
    position: absolute;
    top: 130px;
    width: 379px;
    height: 622px;
    overflow: hidden;
  }
  .carton--dark { left: 122px; background: var(--box-dark); }
  .carton--light { left: 672px; background: var(--box-light); outline: 1px solid #d6d6d6; }

  .carton__texture {
    position: absolute;
    inset: 0;
  }
  .carton--dark .carton__texture { background: linear-gradient(160deg, #1e1e1e, #0e0e0e); }
  .carton--light .carton__texture { background: linear-gradient(160deg, #f8f8f8, #efefef); }

  .oil-drip {
    position: absolute;
    top: 88px;
    left: 116px;
    width: 148px;
    height: 70px;
    border-radius: 0 0 30px 30px / 0 0 60px 60px;
    background: linear-gradient(180deg, var(--oil), #e9a514);
  }

  .claim-band {
    position: absolute;
    top: 0;
    left: 62px;
    width: 255px;
    height: 112px;
  }
  .claim-band__shape {
    position: absolute;
    inset: 0;
    width: 255px;
    height: 112px;
  }
  .claim-band__text {
    position: absolute;
    inset: 0;
    display: flex;
    flex-direction: column;
    align-items: center;
    font-family: "Rye", serif;
    color: var(--cream);
    white-space: nowrap;
  }
  .claim-band__tested {
    margin-top: 18px;
    font-size: 11px;
    border: 1px solid currentColor;
    padding: 1px 6px;
    line-height: 1.1;
  }
  .claim-band__product {
    margin-top: 8px;
    font-size: 15px;
    line-height: 1;
  }
  .claim-band__dose {
    margin-top: 8px;
    font-family: "Open Sans", sans-serif;
    font-weight: 700;
    font-size: 11px;
    line-height: 1.4;
    letter-spacing: 3px;
    border: 1px solid currentColor;
    padding: 0 10px;
  }
  .carton--dark .claim-band__dose { color: var(--dose-dark); }
  .carton--light .claim-band__dose { color: var(--lime); }

  .brand-name {
    position: absolute;
    left: 0;
    right: 0;
    text-align: center;
    font-family: "Open Sans", sans-serif;
    font-weight: 700;
    font-size: 44px;
    letter-spacing: 1px;
    line-height: 1;
    white-space: nowrap;
  }
  .carton--dark .brand-name { top: 296px; color: var(--gold); }
  .carton--light .brand-name { top: 312px; color: var(--lime); }

  .thc-symbol {
    position: absolute;
    width: 62px;
    height: 58px;
    left: 158px;
  }
  .carton--dark .thc-symbol { top: 444px; }
  .carton--light .thc-symbol { top: 458px; }

  .net-weight {
    position: absolute;
    left: 0;
    right: 0;
    text-align: center;
    font-family: "Open Sans", sans-serif;
    font-weight: 700;
    font-size: 12px;
    color: var(--mark-grey);
    letter-spacing: 0.3px;
  }
  .carton--dark .net-weight { top: 548px; }
  .carton--light .net-weight { top: 564px; }

  .option-label {
    position: absolute;
    top: 774px;
    width: 379px;
    text-align: center;
    font-family: "Open Sans", sans-serif;
    font-size: 36px;
    color: var(--label-grey);
  }
  .option-label--dark { left: 122px; }
  .option-label--light { left: 672px; }
</style>
</head>
<body>
<main class="canvas">

  <section class="carton carton--dark">
    <div class="carton__texture" role="img" aria-label="Dark embossed damask pattern with diagonal sheen"></div>
    <div class="oil-drip" role="img" aria-label="Illustration of golden oil dripping from the band"></div>
    <div class="claim-band">
      <svg class="claim-band__shape" viewBox="0 0 255 112" aria-hidden="true">
        <path d="M0 0 H255 V94 Q127.5 116 0 94 Z" fill="var(--leaf-green)"/>
      </svg>
      <div class="claim-band__text">
        <span class="claim-band__tested">LAB TESTED</span>
        <span class="claim-band__product">PREMIUM CANNABIS OIL</span>
        <span class="claim-band__dose">500MG</span>
      </div>
    </div>
    <div class="brand-name">COPPER MIST</div>
    <svg class="thc-symbol" viewBox="0 0 62 58" aria-hidden="true">
      <path d="M31 4 L58 52 H4 Z" fill="none" stroke="var(--mark-grey)" stroke-width="4" stroke-linejoin="round"/>
    </svg>
    <div class="net-weight">NET WT .5G</div>
  </section>

  <section class="carton carton--light">
    <div class="carton__texture" role="img" aria-label="White embossed damask pattern"></div>
    <div class="oil-drip" role="img" aria-label="Illustration of golden oil dripping from the band"></div>
    <div class="claim-band">
      <svg class="claim-band__shape" viewBox="0 0 255 112" aria-hidden="true">
        <path d="M0 0 H255 V94 Q127.5 116 0 94 Z" fill="var(--band-dark)"/>
      </svg>
      <div class="claim-band__text">
        <span class="claim-band__tested">LAB TESTED</span>
        <span class="claim-band__product">PREMIUM CANNABIS OIL</span>
        <span class="claim-band__dose">500MG</span>
      </div>
    </div>
    <div class="brand-name">COPPER MIST</div>
    <svg class="thc-symbol" viewBox="0 0 62 58" aria-hidden="true">
      <path d="M31 4 L58 52 H4 Z" fill="none" stroke="var(--mark-grey)" stroke-width="4" stroke-linejoin="round"/>
    </svg>
    <div class="net-weight">NET WT .5G</div>
  </section>

  <div class="option-label option-label--dark">Option 01</div>
  <div class="option-label option-label--light">Option 01</div>

</main>
</body>
</html>
```